Personal training and nutrition business needs business card design

We need a business card that outlays our services and invites potential customers to join our team and take the first step to a healthier and more enjoyable life. We cater for any level of fitness and specialize in weight loss and conditioning, strength training, muscle gain and strength endurance. Whether you are just starting off or need some help getting to the next level of your journey we are here to get the job done.
We specialize in one on one or one on two personal training sessions and each program will be custom made to suit individual fitness goals of our clients

```html
<!DOCTYPE html>
<html lang="en">
<head>
<meta charset="utf-8">
<title>Stride &amp; Core – Business Card</title>
<link rel="stylesheet" href="https://fonts.googleapis.com/css2?family=Arimo:wght@400;700&family=Oswald:wght@400&display=swap">
<style>
  :root {
    --page: #e4e4e4;
    --card: #2e2e30;
    --card-deep: #262628;
    --ink: #ffffff;
    --violet: #8e4fc0;
    --orchid: #b363c4;
    --rule: #8a8a8c;
  }
  * { box-sizing: border-box; margin: 0; padding: 0; }
  html, body { width: 1200px; height: 801px; overflow: hidden; }
  body {
    background: var(--page);
    font-family: "Arimo", Arial, sans-serif;
    position: relative;
  }
  .card {
    position: absolute;
    top: 246px;
    width: 540px;
    height: 309px;
    background: var(--card);
    border-bottom: 5px solid var(--violet);
    border-image: linear-gradient(90deg, var(--violet), var(--orchid)) 1;
    box-shadow: 0 10px 24px rgba(0,0,0,.18);
    overflow: hidden;
  }
  .card--front { left: 40px; }
  .card--back {
    left: 620px;
    background: radial-gradient(circle at 30% 40%, #3a3a3c 0%, var(--card) 45%, var(--card-deep) 100%);
  }

  /* front */
  .brand {
    position: absolute;
    left: 40px;
    top: 44px;
  }
  .brand__row { display: flex; align-items: center; gap: 12px; }
  .brand__mark {
    width: 38px; height: 38px;
    background: linear-gradient(135deg, var(--orchid), var(--violet));
    border-radius: 6px;
  }
  .brand__name {
    color: var(--ink);
    font-weight: 700;
    font-size: 27px;
    letter-spacing: 1px;
    text-transform: uppercase;
  }
  .brand__tagline {
    margin-top: 8px;
    font-family: "Oswald", "Arial Narrow", sans-serif;
    font-size: 9.5px;
    letter-spacing: 1.6px;
    color: var(--orchid);
    text-transform: uppercase;
  }
  .person { position: absolute; left: 40px; top: 148px; }
  .person__name {
    font-weight: 700;
    font-size: 23px;
    color: var(--violet);
    text-transform: uppercase;
    letter-spacing: .5px;
  }
  .person__role { font-size: 16px; color: var(--ink); margin-top: 4px; }

  .divider {
    position: absolute;
    left: 292px; top: 112px;
    width: 1px; height: 104px;
    background: var(--rule);
  }
  .contact {
    position: absolute;
    left: 312px; top: 118px;
    list-style: none;
  }
  .contact li {
    display: flex; align-items: center; gap: 10px;
    color: var(--ink);
    font-size: 15px;
    height: 32px;
  }
  .contact svg { width: 14px; height: 14px; flex: none; }
  .address {
    position: absolute;
    left: 40px; bottom: 36px;
    color: var(--ink);
    font-size: 16px;
  }

  /* back */
  .back-brand {
    position: absolute;
    right: 36px; bottom: 54px;
    text-align: left;
  }
  .back-brand__name {
    color: var(--ink);
    font-weight: 700;
    font-size: 40px;
    line-height: 1.05;
    letter-spacing: 1.5px;
    text-transform: uppercase;
  }
  .back-brand__tagline {
    margin-top: 10px;
    font-family: "Oswald", "Arial Narrow", sans-serif;
    font-size: 11px;
    letter-spacing: 1.8px;
    color: var(--orchid);
    text-transform: uppercase;
  }
</style>
</head>
<body>
  <section class="card card--front">
    <div class="brand">
      <div class="brand__row">
        <span class="brand__mark"></span>
        <span class="brand__name">Stride &amp; Core</span>
      </div>
      <p class="brand__tagline">Personal training. Nutrition. Motivation</p>
    </div>

    <div class="person">
      <p class="person__name">Marcus Reyes</p>
      <p class="person__role">Manager</p>
    </div>

    <span class="divider"></span>

    <ul class="contact">
      <li>
        <svg viewBox="0 0 24 24" fill="none" stroke="#8e4fc0" stroke-width="2.4" stroke-linecap="round" stroke-linejoin="round"><path d="M5 3h4l2 5-3 2a11 11 0 0 0 6 6l2-3 5 2v4a2 2 0 0 1-2 2A17 17 0 0 1 3 5a2 2 0 0 1 2-2z"/></svg>
        555-010-2100
      </li>
      <li>
        <svg viewBox="0 0 24 24" fill="none" stroke="#8e4fc0" stroke-width="2.2" stroke-linejoin="round"><rect x="2" y="5" width="20" height="14" rx="1"/><path d="M2 6l10 7 10-7"/></svg>
        hello@strideandcore.com
      </li>
      <li>
        <svg viewBox="0 0 24 24" fill="none" stroke="#8e4fc0" stroke-width="2"><circle cx="12" cy="12" r="10"/><path d="M2 12h20M12 2c3 3 3 17 0 20M12 2c-3 3-3 17 0 20"/></svg>
        www.strideandcore.com
      </li>
    </ul>

    <p class="address">Your address, city, state, ZIP 0000</p>
  </section>

  <section class="card card--back">
    <div class="back-brand">
      <p class="back-brand__name">Stride<br>&amp; Core</p>
      <p class="back-brand__tagline">Personal training. Nutrition. Motivation</p>
    </div>
  </section>
</body>
</html>
```